International Internship Provider Needs Catalogue Layout & Design

We need a catalogue/booklet created to send out to university students and study abroad offices. We provide international internships to university students and young professionals in a range of fields in nine cities across the globe. Our program includes guaranteed internship, accommodation, social events, and support from staff. We would like to provide a clean, glossy, and picture-heavy publication to promote our program and website. We'd like to use captivating colors and the final product should convey what our program does and express the fun of living abroad with the professionalism of an internship.

Reason: We've increased the budget by $100, and we understand the project is a large undertaking. Thank you!

We would like each location to be two pages with large images of that location as well as all of the copy in the word document attached. Attached on the images is as an example of another catalogue we liked the style of for you to look at it. If you need any more details or would like me to break up the copy into sections please do not hesitate to ask. thank you!  

I've added new file of content that includes everything in the previous file plus more information, but on separate pages to help make it clear what information goes together. The location should still be a two-page spread that includes a large location image. We would like to have a quote from a student on each of those pages as well. 

I've added more photos for the location pages labeled by the location (ex: London_girls). I've also added some photos for Project Kelvo and new content. Please contact me with any questions. 

Reason: We realized we've asked for a few more edits from designers and we appreciate the time it takes to be make these constant edits. Thank you!

University students and recent college graduates. Usually the target market is between 21-23 years of age, and most students who travel abroad are female.

University

• It must be at least 10 pages and use the logo I've attached. Please be sure to look at the word document that is full of content that will be used in the project. Large photos of the locations are ideal as well 2 pages for each location.
• I have loads of photos I can give to you to use in the document, but you can use placeholders for now or some of the photos I've attached. I've also included a document full of copy that will need to be in the document just to give you an idea of where things will be displayed.

```html
<!DOCTYPE html>
<html lang="en">
<head>
<meta charset="utf-8">
<title>Why Intern with Project Kelvo</title>
<link rel="stylesheet" href="https://fonts.googleapis.com/css2?family=Zilla+Slab:wght@300&family=Lato:ital,wght@1,400;1,700&display=swap">
<style>
  :root {
    --sky: #b8d3ec;
    --mid: #5c7fa8;
    --navy: #16365e;
    --deep: #123258;
    --white: #ffffff;
    --footer: #f1f2f4;
    --pill: rgba(150, 168, 196, 0.75);
    --pill-edge: rgba(255, 255, 255, 0.7);
    --brand: #1d3a66;
  }
  * { margin: 0; padding: 0; box-sizing: border-box; }
  html, body { width: 848px; height: 1200px; overflow: hidden; }
  body { background: var(--footer); font-family: "Lato", sans-serif; }
  .page {
    position: relative;
    width: 848px;
    height: 1200px;
    overflow: hidden;
  }
  .panel {
    position: absolute;
    inset: 0 0 90px 0;
    background: linear-gradient(180deg, var(--sky) 0%, #7f9fc6 14%, var(--mid) 32%, #34577f 60%, var(--navy) 85%, var(--deep) 100%);
  }
  .footer {
    position: absolute;
    left: 0; right: 0; bottom: 0;
    height: 90px;
    background: var(--footer);
    border-top: 1px solid #d5d9df;
  }
  .page-title {
    position: absolute;
    right: 45px;
    top: 18px;
    font-family: "Zilla Slab", serif;
    font-weight: 300;
    font-size: 66px;
    line-height: 80px;
    color: var(--white);
    text-align: right;
  }
  .section { position: absolute; left: 31px; width: 788px; }
  .section-label {
    display: block;
    width: 256px;
    height: 35px;
    margin: 0 auto;
    border-radius: 10px;
    background: var(--pill);
    border: 1px solid var(--pill-edge);
    box-shadow: 0 1px 3px rgba(0,0,0,0.2);
    color: var(--white);
    font-weight: 700;
    font-style: italic;
    font-size: 15.5px;
    line-height: 33px;
    text-align: center;
  }
  .section-copy {
    margin-top: 13px;
    color: var(--white);
    font-style: italic;
    font-size: 15.3px;
    line-height: 21.4px;
    text-align: justify;
    text-align-last: center;
    hyphens: auto;
  }
  .s-guarantee { top: 241px; }
  .s-career { top: 366px; }
  .s-support { top: 590px; }
  .s-social { top: 776px; }
  .s-staff { top: 938px; }
  .brand {
    position: absolute;
    right: 52px;
    bottom: 26px;
    display: flex;
    align-items: center;
    gap: 10px;
    font-family: "Lato", sans-serif;
    font-style: italic;
    font-weight: 700;
    font-size: 19px;
    color: var(--brand);
  }
  .brand-dot { width: 36px; height: 36px; }
</style>
</head>
<body>
<main class="page">
  <div class="panel"></div>
  <div class="footer"></div>

  <h1 class="page-title">Why Intern with<br>Project Kelvo</h1>

  <section class="section s-guarantee">
    <h2 class="section-label">Guaranteed Internships</h2>
    <p class="section-copy">If accepted into the program, we can guarantee you an internship within your field. We work directly with our host employers to communicate your qualifications, interests, goals, and strengths to find you the best possible internship placement. We have 100% placement success rate for over 10 years.</p>
  </section>

  <section class="section s-career">
    <h2 class="section-label">3-Phase Career Development</h2>
    <p class="section-copy">Before, during, and after the internship program all of our interns will receive professional career development to prepare them for the internship and their professional careers after university. All of our participants will work with a Program Advisor to establish career objectives, discuss industry trends, receive personal resume and cover letter training and interview preparation. Through a partnership with Brightline Research, all of our participants will also have access to the Strength Compass assessment to learn their top 5 Strengths within the workplace. During the programs the career development continues with unique coaching and hands on events to give you an edge for your career.</p>
  </section>

  <section class="section s-support">
    <h2 class="section-label">Individualized Support</h2>
    <p class="section-copy">Starting from the first phone call, we work with you one-on-one to learn about your personal interests and career objectives. Our Program Advisors will provide visa support, pre-departure information, and answer any questions through phone calls and a series of webinars. Once in your new home, our Location Coordinators will have an orientation for you and will be available to you 24/7 as an emergency contact.</p>
  </section>

  <section class="section s-social">
    <h2 class="section-label">Social Events &amp; Excursions</h2>
    <p class="section-copy">An internship is hard work, but we have planned several city-specific events and excursions to help you foster new relationships with other interns and enjoy all that you host city has to offer. We give you the insiders guide to your new city since all our staff are locals and they give you the best mix of must dos and one of a kind experiences. Social events may range from trekking through the Blue Mountains in Sydney, dinning on homemade pasta in Florence, or pouring the perfect pint in Dublin.</p>
  </section>

  <section class="section s-staff">
    <h2 class="section-label">Local Staff</h2>
    <p class="section-copy">In each of our nine locations, we have local staff that is there to ensure that all aspects of the program are fulfilled for each participant. Our Location Coordinators live in that city year-round and can provide you with a real insider's advice about local customs, the language, places to see, and where to shop. Our Location Coordinators are in daily communication with our home office in Port Ellis, MD so you know all our staff is updated on your internship and time abroad.</p>
  </section>

  <div class="brand">
    <svg class="brand-dot" viewBox="0 0 36 36" aria-hidden="true"><circle cx="18" cy="18" r="17" fill="#1d3a66"/></svg>
    <span>Project Kelvo</span>
  </div>
</main>
</body>
</html>
```